**Kestrel Joinery Works Limited**

We need a website for a renovation/remodeling company based in Hamilton, New Zealand. Ideally it will catch clients' attention and be modern and professional looking. I have attached a logo that I have just recently had made (through PixelForge). If the website could reflect this style and colour schemes, that would be awesome. The final design should communicate a trustworthiness and professionalism.

I have attached photos of a website that I really think is great, so if we could have something that follows along those likes,

https://www.dailyquillpost.example/local-news/news/hamilton-builder-named-top-apprentice-in-region/QXPLTZ8VRA3MJ5FDYHUNCESKWB/

I won a competition a few years ago while I was an apprentice, If we could somehow put that in there as one of my achievements to try to bring in some trust that would be awesome. I would like to add a new picture though because my beard in that photo is wild.

Target Market(s)

Families that want live in the homes that i'm working on. not investors. People that are looking for quality not cheapest price.

Industry/Entity Type

Construction, Home renovations, Maintenance, Deck Builds, New Builds, Bathrooms, Kitchens

Coding

Number of Pages Required

5+ page

Font styles to use
Sans Serif

Colors
6B429C
8869AF
B7A5CE
E3DAEB
F3F0F8

Requirements
Must have
• Contact us page, large clear pictures, Colours the work with the purple in my logo. That will be my company colour so I'm thinking black and purple, or what ever compliments purple nicely
Nice to have
• Page for Renovations, Testimonials, Contact us, Home, About us
Should not have
• Plain looking pages, empty white space, I want the text to be beside a nice big picture etc

```html
<!DOCTYPE html>
<html lang="en">
<head>
<meta charset="utf-8">
<title>Kestrel Joinery Works Ltd</title>
<link href="https://fonts.googleapis.com/css2?family=Montserrat:wght@400;500;600;700;800&display=swap" rel="stylesheet">
<style>
:root{
  --purple:#6B429C;
  --purple-mid:#8869AF;
  --purple-soft:#B7A5CE;
  --purple-pale:#E3DAEB;
  --purple-mist:#F3F0F8;
  --ink:#1c1c1e;
  --text:#3a3a3c;
  --muted:#8a8a8e;
  --dark:#3b3a3c;
  --line:#d9d9dc;
  --footer-bg:#f4f3f2;
  --white:#ffffff;
}
*{box-sizing:border-box;margin:0;padding:0}
html,body{width:1200px;height:4368px;overflow:hidden}
body{position:relative;background:var(--white);font-family:'Montserrat',sans-serif;color:var(--text)}
.abs{position:absolute}
a{color:inherit;text-decoration:none}

/* header / hero */
.hero{position:absolute;left:0;top:0;width:1200px;height:712px;
  background:linear-gradient(180deg,#f6f6f9 0%,#e6e5ec 35%,#d8d6de 62%,#f2f1f4 85%,#fff 100%)}
.hero-photo{position:absolute;inset:0;
  background:radial-gradient(ellipse at 60% 70%,rgba(190,186,198,.55),transparent 60%),
             linear-gradient(90deg,rgba(210,214,226,.8) 0%,transparent 22%,transparent 78%,rgba(150,170,140,.35) 88%,rgba(220,220,228,.6) 100%)}
.hero-fade{position:absolute;left:0;right:0;bottom:0;height:160px;background:linear-gradient(180deg,transparent,#fff)}
.nav a{position:absolute;top:64px;font-size:15px;font-weight:500;color:var(--ink);letter-spacing:.2px}
.btn{display:flex;align-items:center;justify-content:center;gap:12px;background:var(--purple);color:#fff;font-size:15px;font-weight:500;letter-spacing:.3px}
.nav-contact{position:absolute;left:912px;top:47px;width:136px;height:50px}
.brand{position:absolute;display:flex;flex-direction:column;align-items:center;color:var(--purple);font-weight:800;text-align:center;line-height:1.05}
.brand-mark{width:26px;height:26px;background:var(--purple);margin-bottom:8px}
.hero-title{position:absolute;left:0;width:1200px;top:252px;text-align:center;font-size:37px;font-weight:500;letter-spacing:1px;color:var(--ink)}
.hero-rule{position:absolute;left:525px;top:307px;width:150px;height:3px;background:var(--purple)}
.hero-sub{position:absolute;left:340px;width:520px;top:320px;text-align:center;font-size:18px;line-height:24px;color:#4a4a4e}

/* about */
.section-title{font-size:29px;font-weight:800;color:var(--ink);letter-spacing:.6px}
.about-bar{left:136px;top:756px;width:3px;height:83px;background:var(--purple)}
.about-title{left:156px;top:748px}
.about-kicker{left:156px;top:795px;width:360px;font-size:15px;font-weight:600;line-height:24px;color:var(--ink)}
.about-body{left:156px;top:868px;width:360px;font-size:15px;line-height:23.6px;color:#5a5a5e}
.read-more{position:absolute;left:156px;top:1100px;width:169px;height:49px}
.about-frame{left:627px;top:731px;width:429px;height:398px;border:7px solid var(--purple);border-left:none;border-bottom:none}
.about-photo{left:607px;top:741px;width:441px;height:408px;background:linear-gradient(135deg,#d8d5cc,#ecebe6 45%,#9aa89a 70%,#e5e3dd)}
.award-card{left:551px;top:1075px;width:436px;height:120px;background:#fff;border-radius:60px 30px 0 0;box-shadow:0 6px 20px rgba(0,0,0,.06)}
.award-badge{left:551px;top:1070px;width:128px;height:128px;border-radius:50%;background:radial-gradient(circle,#3a3a3a 55%,#b8923a 57%,#e2c27a 64%,#8d6b2a 68%)}
.award-name{left:702px;top:1096px;font-size:23px;font-weight:700;color:var(--ink)}
.award-quote{left:702px;top:1136px;width:270px;font-size:12.5px;line-height:21px;color:#3a3a3c;font-weight:500}

/* vision */
.vision{left:0;top:1254px;width:1200px;height:729px;
  background:linear-gradient(180deg,#fff 0%,#eef0f4 18%,#e7e9ee 60%,#f1f2f5 88%,#fff 100%)}
.centered{left:0;width:1200px;text-align:center}
.divider{position:absolute;left:470px;width:260px;height:20px}
.divider::before,.divider::after{content:"";position:absolute;top:9px;width:86px;height:2px;background:var(--purple-soft)}
.divider::before{left:0}.divider::after{right:0}
.divider span{position:absolute;left:120px;top:0;width:20px;height:20px;background:var(--dark);border-bottom:4px solid var(--purple)}
.vision-text{left:251px;top:1446px;width:712px;text-align:center;font-size:15px;line-height:24px;color:#2f2f32}
.card{position:absolute;top:1587px;width:210px;height:244px;background:rgba(255,255,255,.82);border:3px solid #fff;box-shadow:0 4px 18px rgba(0,0,0,.06);padding:20px 14px}
.card svg{width:40px;height:40px;display:block}
.card h3{margin-top:12px;font-size:14.5px;font-weight:700;color:var(--ink);line-height:20px;letter-spacing:.2px}
.card p{margin-top:14px;font-size:11.5px;line-height:18.5px;color:#8e8e92}

/* services */
.svc-bar{left:146px;top:2102px;width:7px;height:540px;background:var(--purple)}
.svc-photo{left:156px;top:2101px;width:376px;height:552px;background:linear-gradient(180deg,#f3f2ef 0%,#e9e5dd 48%,#d8c7ab 62%,#f0ede8 100%)}
.svc-badge{left:429px;top:2091px;width:142px;height:142px;border-radius:50%;background:#fff;border:6px solid #2e2e30;box-shadow:0 0 0 3px #fff}
.svc-badge::after{content:"";position:absolute;left:32px;top:32px;width:66px;height:66px;border-radius:50%;background:#2e2e30}
.svc-title{left:595px;top:2122px;width:460px;line-height:42px}
.svc-text{left:595px;top:2222px;width:450px;font-size:15px;line-height:24px;color:#2f2f32}
.svc-tile{position:absolute;top:2345px;width:214px}
.svc-tile .ph{height:198px}
.svc-tile .lbl{margin-top:24px;font-size:15px;font-weight:600;color:var(--ink);letter-spacing:.4px}
.arrows{left:932px;top:2630px;width:117px;height:25px;display:flex;gap:2px}
.arrows div{flex:1;border:1px solid #b8b8bc;display:flex;align-items:center;justify-content:center}

/* projects */
.proj-side{top:2896px;height:342px}
.proj-main{left:242px;top:2862px;width:714px;height:410px;background:linear-gradient(180deg,#f4f4f2 0%,#e7e7e4 45%,#5f88b8 55%,#dfe2e3 80%)}
.proj-panel{left:242px;top:3103px;width:614px;height:169px;background:var(--dark);padding:28px 37px}
.proj-corner{left:242px;top:3087px;width:0;height:0;border-left:22px solid var(--purple-mid);border-top:22px solid transparent}
.proj-panel h3{font-size:18px;font-weight:600;color:#fff;letter-spacing:1.4px}
.proj-panel p{margin-top:14px;font-size:13px;line-height:21px;color:#e2e2e4}
.proj-panel a{display:inline-block;margin-top:8px;font-size:14px;color:#fff;letter-spacing:.4px;border-bottom:1px solid #fff;padding-bottom:2px}
.dots{left:555px;top:3345px;display:flex;gap:12px}
.dots i{width:13px;height:13px;border-radius:50%;border:1px solid #b8b8bc;display:block}
.dots i.on{border-color:var(--purple);background:radial-gradient(circle,var(--purple) 45%,#fff 50%)}

/* contact */
.cta-title{top:3474px;line-height:40px}
.footer-bg{left:0;top:3853px;width:1200px;height:515px;background:var(--footer-bg)}
.contact-box{left:151px;top:3590px;width:897px;height:408px;background:#fff;box-shadow:0 8px 30px rgba(0,0,0,.07)}
.contact-info{left:151px;top:3590px;width:322px;height:408px;background:var(--dark);padding:0 32px;color:#fff}
.contact-info h2{position:absolute;left:32px;top:44px;font-size:29px;font-weight:600}
.info-row{position:absolute;left:32px;display:flex;gap:14px}
.info-row svg{width:18px;height:18px;flex:none;margin-top:1px}
.info-row b{display:block;font-size:15px;font-weight:600}
.info-row span{display:block;margin-top:5px;font-size:14px;line-height:23px;color:#bdbdc0;width:210px}
.form-title{left:519px;top:3628px;font-size:19px;font-weight:600;color:var(--ink)}
.field{position:absolute;border:1px solid var(--line);font-size:13px;color:#3a3a3c;padding:10px 18px}
.submit{position:absolute;left:824px;top:3914px;width:180px;height:49px}

/* footer */
.foot-social{top:4223px;width:25px;height:25px;border-radius:50%;border:2px solid #6b6b70}
.foot-col{position:absolute;top:4078px;border-left:3px solid var(--purple);padding-left:19px}
.foot-col h4{font-size:15px;font-weight:700;color:var(--ink);letter-spacing:.3px;line-height:18px}
.foot-col ul{list-style:none;margin-top:24px;margin-left:-3px}
.foot-col li{font-size:13.5px;color:#6b6b70;line-height:24.6px}
.foot-rule{left:151px;top:4302px;width:897px;height:1px;background:#dcdcdc}
.copyright{top:4323px;font-size:13px;color:#5a5a5e}
</style>
</head>
<body>

<header class="hero">
  <div class="hero-photo" role="img" aria-label="Bright modern living room with sofa, coffee table and large windows"></div>
  <div class="hero-fade"></div>
  <nav class="nav">
    <a href="#" style="left:156px">HOME</a>
    <a href="#" style="left:251px">ABOUT US</a>
    <a href="#" style="left:378px">SERVICES</a>
    <a href="#" style="left:765px">TESTIMONISLS</a>
  </nav>
  <a href="#" class="btn nav-contact">CONTACT US</a>
  <div class="brand" style="left:470px;top:40px;width:260px;font-size:21px">
    <div class="brand-mark"></div>
    <div>KESTREL JOINERY</div>
    <div style="font-size:16px;margin-top:4px">WORKS LTD</div>
  </div>
  <h1 class="hero-title">KESTREL JOINERY WORKS LTD</h1>
  <div class="hero-rule"></div>
  <p class="hero-sub">Your Trusted Partner in Home Renovations and Building Excellence</p>
</header>

<section class="about">
  <div class="abs about-bar"></div>
  <h2 class="abs section-title about-title">ABOUT US</h2>
  <p class="abs about-kicker">Bringing Your Vision to Life with Quality Renovations and Construction</p>
  <p class="abs about-body">At Kestrel Joinery Works LTD, we take pride in our ability to turn your dreams into reality. Our commitment to quality and dedication to craftsmanship are the cornerstones of our service. With years of experience, a winning spirit, and a passion for creating exceptional living spaces, we are your trusted partner in home renovations and construction.</p>
  <a href="#" class="btn read-more">READ MORE
    <svg width="28" height="12" viewBox="0 0 28 12" fill="none" stroke="#fff" stroke-width="1.8"><path d="M0 6h26M21 1l5 5-5 5"/></svg></a>
  <div class="abs about-frame"></div>
  <div class="abs about-photo" role="img" aria-label="Smiling builder standing in a doorway of a renovated living room"></div>
  <div class="abs award-card"></div>
  <div class="abs award-badge" role="img" aria-label="Gold top apprentice award medal"></div>
  <div class="abs award-name">Mason Hale</div>
  <p class="abs award-quote">"Waikato's top building apprentice" at the Northfield Apprentice Challenge</p>
</section>

<section>
  <div class="abs vision" role="img" aria-label="Soft white modern bathroom with basin and freestanding bath"></div>
  <h2 class="abs section-title centered" style="top:1346px">YOUR VISION, OUR EXPERTISE</h2>
  <div class="divider" style="top:1398px"><span></span></div>
  <p class="abs vision-text">At Kestrel Joinery Works LTD, we understand that our target market consists of families seeking quality homes, not just investors looking for a quick profit. We know that your home is more than just a building; it's where you create cherished memories and lay the foundation for your family's future. That's why we offer:</p>

  <div class="card" style="left:152px">
    <svg viewBox="0 0 40 40" fill="none" stroke="#6B429C" stroke-width="2.6"><circle cx="20" cy="21" r="16"/><path d="M11 22l9-8 9 8M14 20v9h12v-9" fill="#6B429C"/></svg>
    <h3>CUSTOMIZED<br>SOLUTIONS</h3>
    <p>We work closely with you to understand your unique needs and preferences, tailoring our services to create a home that perfectly suits your family.</p>
  </div>
  <div class="card" style="left:381px">
    <svg viewBox="0 0 40 40" fill="#6B429C"><circle cx="20" cy="14" r="11"/><circle cx="20" cy="14" r="5" fill="#fff"/><path d="M12 22l-5 14 6-2 3 5 4-12zM28 22l5 14-6-2-3 5-4-12z"/></svg>
    <h3>QUALITY<br>CRAFTSMANSHIP</h3>
    <p>We prioritize top-notch materials and employ skilled craftsmen to ensure that every aspect of your home meets the highest standards of quality and durability.</p>
  </div>
  <div class="card" style="left:609px">
    <svg viewBox="0 0 40 40" fill="#6B429C"><path d="M2 22l10-9 10 9h-3v12H5V22z"/><path d="M18 18l11-11 11 11h-3v16H21V18z"/><rect x="26" y="22" width="6" height="6" fill="#fff"/></svg>
    <h3>ATTENTION TO<br>DETAIL</h3>
    <p>Families looking for quality homes appreciate the finer details, and we take great care to ensure that every element of your project exceeds your expectations.</p>
  </div>
  <div class="card" style="left:837px">
    <svg viewBox="0 0 40 40" fill="#6B429C"><circle cx="16" cy="13" r="8"/><path d="M2 36c0-9 6-14 14-14s14 5 14 14z"/><path d="M26 4h12v9h-6l-4 4v-4h-2z"/></svg>
    <h3>EXPERT<br>CONSULTATION</h3>
    <p>We offer professional guidance to help you make informed decisions about design, materials, and more.</p>
  </div>
</section>

<section>
  <div class="abs svc-bar"></div>
  <div class="abs svc-photo" role="img" aria-label="White kitchen with open shelves, pendant lights and timber benchtop"></div>
  <div class="abs svc-badge" role="img" aria-label="Licensed practitioner badge"></div>
  <h2 class="abs section-title svc-title">OUR COMPREHENSIVE SERVICES</h2>
  <p class="abs svc-text">Whether you're looking to transform your current space or embark on a new project, we have the expertise and dedication to make it a reality. Our services include:</p>
  <div class="svc-tile" style="left:595px">
    <div class="ph" role="img" aria-label="Renovated living room with grey sofa and pendant light" style="background:linear-gradient(135deg,#cfc7bb,#8f8475 55%,#c9853f 75%,#e0dbd2)"></div>
    <div class="lbl">HOME RENOVATIONS</div>
  </div>
  <div class="svc-tile" style="left:834px">
    <div class="ph" role="img" aria-label="Room under maintenance with ladder and timber floor" style="background:linear-gradient(90deg,#bdbdbd,#8b8b8b 40%,#d8d6d2 60%,#a8774f 100%)"></div>
    <div class="lbl">MAINTENANCE</div>
  </div>
  <div class="svc-tile" style="left:1073px;width:127px;overflow:hidden">
    <div class="ph" role="img" aria-label="Timber deck outside a house" style="background:linear-gradient(180deg,#a9c8e3,#5a6e8c 45%,#a55a34 80%,#c98b5c)"></div>
    <div class="lbl" style="white-space:nowrap">DECK BUILDS</div>
  </div>
  <div class="abs arrows">
    <div><svg width="38" height="12" viewBox="0 0 38 12" fill="none" stroke="#1c1c1e" stroke-width="1.8"><path d="M38 6H2M7 1L2 6l5 5"/></svg></div>
    <div><svg width="38" height="12" viewBox="0 0 38 12" fill="none" stroke="#6B429C" stroke-width="1.8"><path d="M0 6h36M31 1l5 5-5 5"/></svg></div>
  </div>
</section>

<section>
  <h2 class="abs section-title centered" style="top:2743px">RECENT PROJECTS</h2>
  <div class="divider" style="top:2813px"><span></span></div>
  <div class="abs proj-side" style="left:0;width:217px;background:linear-gradient(90deg,#efeeec,#d9c6a8 55%,#f3f2f0)" role="img" aria-label="Bright room with timber slat wall"></div>
  <div class="abs proj-side" style="left:981px;width:219px;background:linear-gradient(90deg,#efece6,#b7ae9c 35%,#ece9e4 70%)" role="img" aria-label="Dining room with plant and chairs"></div>
  <div class="abs proj-main" role="img" aria-label="Renovated kitchen with white cabinets and tall glass windows"></div>
  <div class="abs proj-corner"></div>
  <div class="abs proj-panel">
    <h3>KITCHEN RENOVATION</h3>
    <p>Kestrel Joinery Works LTD recently completed a remarkable kitchen renovation that truly stands as a testament to our commitment to quality and excellence.</p>
    <a href="#">LEARN MORE</a>
  </div>
  <div class="abs dots"><i></i><i></i><i class="on"></i><i></i><i></i></div>
</section>

<section>
  <h2 class="abs section-title centered cta-title">READY TO TRANSFORM<br>YOUR SPACE?</h2>
  <div class="abs footer-bg"></div>
  <div class="abs contact-box"></div>
  <div class="abs contact-info">
    <h2>Get In Touch</h2>
    <div class="info-row" style="top:130px">
      <svg viewBox="0 0 24 24" fill="#fff"><path d="M12 2a7 7 0 0 0-7 7c0 5 7 13 7 13s7-8 7-13a7 7 0 0 0-7-7zm0 9.5A2.5 2.5 0 1 1 12 6.5a2.5 2.5 0 0 1 0 5z"/></svg>
      <div><b>Address</b><span>418 Harrow Lane, Millbrook, Waikato 3204</span></div>
    </div>
    <div class="info-row" style="top:226px">
      <svg viewBox="0 0 24 24" fill="#fff"><path d="M6.6 10.8a15 15 0 0 0 6.6 6.6l2.2-2.2a1 1 0 0 1 1-.25 11.4 11.4 0 0 0 3.6.57 1 1 0 0 1 1 1V20a1 1 0 0 1-1 1A17 17 0 0 1 3 4a1 1 0 0 1 1-1h3.5a1 1 0 0 1 1 1c0 1.25.2 2.45.57 3.57a1 1 0 0 1-.25 1z"/></svg>
      <div><b>Phone</b><span>(07) 555-0142</span></div>
    </div>
    <div class="info-row" style="top:300px">
      <svg viewBox="0 0 24 24" fill="#fff"><path d="M3 5h18v14H3z"/><path d="M3 5l9 7 9-7" fill="none" stroke="#3b3a3c" stroke-width="2"/></svg>
      <div><b>Email</b><span>(07) 555-0142</span></div>
    </div>
  </div>
  <h3 class="abs form-title">Drop Your Message</h3>
  <div class="field" style="left:519px;top:3678px;width:234px;height:36px">Your name</div>
  <div class="field" style="left:768px;top:3678px;width:234px;height:36px">Your phone</div>
  <div class="field" style="left:519px;top:3732px;width:483px;height:36px">Your email</div>
  <div class="field" style="left:519px;top:3786px;width:483px;height:102px">Message</div>
  <a href="#" class="btn submit">SUBMIT NOW
    <svg width="26" height="12" viewBox="0 0 26 12" fill="none" stroke="#fff" stroke-width="1.8"><path d="M0 6h24M19 1l5 5-5 5"/></svg></a>
</section>

<footer>
  <div class="brand" style="left:166px;top:4066px;width:210px;font-size:19px">
    <div class="brand-mark"></div>
    <div>KESTREL JOINERY</div>
    <div style="font-size:15px;margin-top:4px">WORKS LTD</div>
  </div>
  <div class="abs foot-social" style="left:225px"></div>
  <div class="abs foot-social" style="left:261px"></div>
  <div class="abs foot-social" style="left:297px"></div>
  <div class="foot-col" style="left:441px"><h4>QUICK LINKS</h4>
    <ul><li>Home</li><li>About Us</li><li>Portfolio</li><li>Testimonials</li><li>Contact Us</li></ul></div>
  <div class="foot-col" style="left:631px"><h4>SERVICES</h4>
    <ul><li>Home Renovations</li><li>Maintenance</li><li>Deck Builds</li><li>Bathrooms</li><li>Kitchens</li><li>Customized Solutions</li></ul></div>
  <div class="foot-col" style="left:846px"><h4>LEGAL</h4>
    <ul><li>Our Team</li><li>FAQ</li><li>Privacy Policy</li><li>Terms and Conditions</li><li>Site Map</li></ul></div>
  <div class="abs foot-rule"></div>
  <p class="abs centered copyright">© 2023 All Rights Reserved | Kestrel Joinery Works LTD</p>
</footer>

</body>
</html>
```